A new customer-driven VC fund for Enterprise IT Startups

I am bringing together a global group of customers (CIOs, CTOs, CISOs of Beacon 3000 companies) to help me identify and diligence best-of-breed Enterprise IT startups so I can invest in them via my new venture capital fund, Larkfen Ventures. In many ways, this is a new model for a VC fund and my goal is to revolutionize Venture Capital so that we hit the bull's eye in investing way more often in what is otherwise a guessing game for most VCs. So in the website, I'd like to capture the essences of global reach, best-of-breed, breakthrough innovation. I also want it to convey the ability of Larkfen Ventures to create category winners (i.e., if you want to be a market leader as a startup, you must take an investment from Larkfen Ventures).
My current website is www.larkfen-ventures.example - please use the content from the website within your design but please DO NOT use the design elements from the current website. INSTEAD, I'm looking for new and creative ideas on how I can leverage the existing content in a more appealing design -- any designs that look remotely similar to the existing website will be immediately declined.
I also want to ensure that the web design is mobile friendly.
Target Market(s)
Startup founders, potential investors, and other VCs
Industry/Entity Type
Venture Capital
Coding
Coded - Design and coding required
Number of Pages Required
1 page
Look and feel
Each slider illustrates characteristics of the customer's brand and the style your logo design should communicate.

```html
<!DOCTYPE html>
<html lang="en">
<head>
<meta charset="utf-8">
<title>Larkfen Ventures</title>
<link href="https://fonts.googleapis.com/css2?family=Poppins:ital,wght@0,300;0,400;0,500;0,600;0,700;1,300;1,500&display=swap" rel="stylesheet">
<style>
:root{
  --canvas:#ebebec;
  --blue-deep:#0b5cc2;
  --blue:#1276d6;
  --cyan:#14b1e7;
  --accent:#1a9bd9;
  --ink:#141a26;
  --muted:#5c6270;
  --navy:#10213a;
  --tint:#e1eff6;
  --line:#dfe5ec;
  --white:#ffffff;
}
*{margin:0;padding:0;box-sizing:border-box}
html,body{width:1200px;height:4347px;overflow:hidden}
body{background:var(--canvas);font-family:'Poppins',sans-serif;color:var(--ink);position:relative}
.page{position:absolute;left:56px;top:37px;width:1088px;height:4273px;background:var(--white);overflow:hidden}
.abs{position:absolute}
.center{text-align:center}

/* hero */
.hero-bg{left:0;top:0;width:1088px;height:530px;background:linear-gradient(120deg,#0a4fb8 0%,#1270d4 45%,#15aee6 100%)}
.hero-band{left:0;top:500px;width:1088px;height:60px}
.brand{display:flex;align-items:center;gap:8px;font-weight:600;font-size:19px;color:var(--white);letter-spacing:.3px;white-space:nowrap}
.brand .dot{width:22px;height:22px;border-radius:50%;background:var(--white)}
.nav{left:509px;top:38px;font-size:11px;color:var(--white);font-weight:500}
.nav a{color:inherit;text-decoration:none;position:absolute;white-space:nowrap}
.btn{left:872px;top:29px;width:102px;height:35px;background:#0c4fb0;color:var(--white);border-radius:3px;font-size:11px;font-weight:600;display:flex;align-items:center;justify-content:center}
.hero-kicker{left:0;width:1088px;top:141px;font-size:30px;font-style:italic;font-weight:300;color:var(--white)}
.hero-title{left:0;width:1088px;top:184px;font-size:38px;font-weight:700;color:var(--white)}
.hero-stage{left:332px;top:245px;width:426px;height:51px;border:2px solid var(--white);color:var(--white);font-size:22px;font-weight:500;letter-spacing:1.5px;display:flex;align-items:center;justify-content:center}
.hero-copy{left:215px;top:333px;width:658px;font-size:12.5px;line-height:23px;color:var(--white)}
.scroll{left:524px;top:512px;width:40px;height:40px;border-radius:50%;background:var(--white);box-shadow:0 2px 10px rgba(0,0,0,.15);display:flex;align-items:center;justify-content:center}

/* headings */
.h2{font-size:34px;font-weight:700;color:var(--ink)}
.h2 .hl{color:var(--accent)}
.rule{width:28px;height:3px;background:var(--ink)}
.lead{font-size:12.5px;line-height:23px;color:#333}

/* who cards */
.card{top:773px;width:272px;height:355px;background:var(--white);border:1px solid var(--line);border-radius:4px;padding:0 24px;text-align:center}
.card.active{border:2px solid var(--accent);box-shadow:0 6px 22px rgba(20,120,200,.12)}
.card svg{display:block;margin:38px auto 0}
.card h3{font-size:17px;font-weight:600;line-height:24px;margin-top:26px;height:48px;display:flex;align-items:center;justify-content:center}
.card p{font-size:11.5px;line-height:19px;color:#555;margin-top:10px}
.dots{background-image:radial-gradient(#c9ced6 1.2px,transparent 1.3px);background-size:9px 9px}

/* strength */
.tint{left:0;top:1264px;width:1088px;height:276px;background:var(--tint)}
.focus-label{left:0;width:1088px;top:1440px;font-size:17px;font-style:italic;font-weight:500;color:#222}
.focus{top:1496px;height:142px;background:var(--white);border:1px solid var(--line);border-radius:3px;box-shadow:0 4px 12px rgba(0,0,0,.06);text-align:center;font-size:11.5px;font-weight:700;line-height:15px;color:#1d2230}
.focus svg{display:block;margin:24px auto 0}
.focus span{position:absolute;left:0;right:0;bottom:24px}
.statement{left:113px;top:1768px;width:350px;font-size:24px;font-weight:600;line-height:37px}
.stat{border-radius:50%;background:var(--white);box-shadow:0 4px 18px rgba(0,0,0,.10);text-align:center;display:flex;flex-direction:column;align-items:center;justify-content:center}
.stat b{font-size:34px;font-weight:700;color:var(--blue-deep);line-height:38px}
.stat small{font-size:10.5px;line-height:15px;color:#444;width:78%}

/* themes */
.themes-title{left:0;width:1088px;top:2378px;font-size:24px;font-weight:600}
.theme{top:2455px;width:300px;text-align:center;font-size:13px;font-weight:600;line-height:20px}
.theme svg{display:block;margin:0 auto 16px}
.vrule{top:2449px;width:1px;height:130px;background:var(--line)}

/* team */
.team-bg{left:0;top:2672px;width:1088px;height:574px;background:linear-gradient(115deg,#0b55bf 0%,#1276d6 55%,#15a9e4 100%)}
.team-title{left:0;width:1088px;top:2743px;font-size:35px;font-weight:700;color:var(--white)}
.team-copy{left:230px;width:628px;top:2816px;font-size:12.5px;line-height:23px;color:var(--white)}
.photo{top:2908px;width:178px;height:166px;border-radius:4px;background:linear-gradient(180deg,#f4f6f8 0%,#d9dee4 100%)}
.person{top:3096px;width:220px;text-align:center;color:var(--white)}
.person b{display:block;font-size:14px;font-weight:600}
.person span{display:block;font-size:11.5px;line-height:16px;margin-top:4px;color:#cfe6fb}
.arrow{top:2980px;color:var(--white);font-size:24px;font-weight:300}

/* engine */
.globe{left:62px;top:3339px;width:405px;height:397px;border-radius:50%;background:radial-gradient(circle at 45% 40%,#f3f8fd 0%,#dcebf8 60%,#c4dcf1 100%)}
.engine-copy{left:543px;top:3417px;width:432px;font-size:12.5px;line-height:23px;color:#333}
.acc{left:543px;width:432px;display:flex;justify-content:space-between;align-items:center;font-size:17px;font-weight:600}
.acc svg{flex:none}
.acc-body{left:543px;top:3548px;width:432px;font-size:11.5px;line-height:20px;color:#555}
.hrule{left:543px;width:432px;height:1px;background:var(--line)}

/* footer */
.footer{left:0;top:3842px;width:1088px;height:431px;background:var(--navy)}
.foot-nav{top:4023px;font-size:12px;color:var(--white);white-space:nowrap}
.foot-mail{left:674px;width:300px;top:4023px;text-align:right;font-size:12px;color:var(--accent);text-decoration:underline;white-space:nowrap}
.foot-rule{left:113px;top:4068px;width:861px;height:1px;background:#243656}
.copy{left:0;width:1088px;top:4100px;font-size:11px;color:#5b6b85}
.copy b{color:var(--white);font-weight:500}
.disclaimer{left:155px;width:776px;top:4148px;font-size:11px;line-height:21px;color:#4c5c77}
</style>
</head>
<body>
<div class="page">

  <!-- HERO -->
  <div class="abs hero-bg" role="img" aria-label="Photo of a business team meeting in an office under a blue overlay"></div>
  <svg class="abs hero-band" viewBox="0 0 1088 60" preserveAspectRatio="none" aria-hidden="true">
    <polygon points="0,30 1088,0 1088,30 0,60" fill="#c9d8ea"/>
    <polygon points="0,45 1088,30 1088,60 0,60" fill="#ffffff"/>
  </svg>
  <div class="abs brand" style="left:113px;top:35px"><span class="dot"></span>Larkfen Ventures</div>
  <nav class="abs nav">
    <a style="left:0">About</a>
    <a style="left:65px">Network</a>
    <a style="left:141px">Team &amp; Advisors</a>
    <a style="left:267px">GTM Engine</a>
  </nav>
  <div class="abs btn">Get Started</div>
  <div class="abs hero-kicker center">We Invest in</div>
  <h1 class="abs hero-title center">Enterprise IT Startups at the</h1>
  <div class="abs hero-stage">PRODUCT - MARKET - FIT STAGE</div>
  <p class="abs hero-copy center">We are singularly focused on helping our portfolio companies gain a massive competitive advantage by providing them access to our exclusive network of hundreds of early-adopting CIOs, CTOs, CISOs, and Channel Partners around the world to rapidly accelerate customer traction.</p>
  <div class="abs scroll"><svg width="12" height="18" viewBox="0 0 12 18"><rect x="1" y="1" width="10" height="16" rx="5" fill="none" stroke="#222" stroke-width="1.4"/><line x1="6" y1="4" x2="6" y2="7" stroke="#222" stroke-width="1.4"/></svg></div>

  <!-- WHO WE ARE -->
  <h2 class="abs h2 center" style="left:0;width:1088px;top:612px"><span class="hl">Who</span> We Are</h2>
  <div class="abs rule" style="left:530px;top:666px"></div>
  <p class="abs lead center" style="left:230px;width:628px;top:684px">We only invest in post-product, post-revenue Enterprise IT startups. Usually, this means you're at Seed Extension to Series A stage.</p>
  <div class="abs dots" style="left:48px;top:752px;width:110px;height:130px"></div>
  <div class="abs dots" style="left:575px;top:1102px;width:110px;height:60px"></div>

  <div class="abs card" style="left:113px">
    <svg width="62" height="56" viewBox="0 0 62 56" fill="none" stroke="#1a7fd0" stroke-width="2"><circle cx="14" cy="8" r="5"/><circle cx="31" cy="8" r="5"/><circle cx="48" cy="8" r="5"/><path d="M6 24v-4a8 8 0 0 1 16 0v4M23 24v-4a8 8 0 0 1 16 0v4M40 24v-4a8 8 0 0 1 16 0v4"/><path d="M4 40l14-8h16l-2 6h-12M32 38l18-8 6 4-22 14H8"/></svg>
    <h3>Customers</h3>
    <p>Hundreds of the earliest-adopting CIOs, CTOs, and CISOs from Beacon 10 to Global 2000 to Cloud-First companies are a part of our exclusive network. An investment from Larkfen Ventures will give you immediate and exclusive access to hundreds of buyers around the world.</p>
  </div>
  <div class="abs card active" style="left:408px">
    <svg width="50" height="56" viewBox="0 0 50 56" fill="none" stroke="#1a7fd0" stroke-width="2"><circle cx="25" cy="13" r="11"/><path d="M25 6v14M21 10h6a2 2 0 0 1 0 4h-4a2 2 0 0 0 0 4h6"/><path d="M25 24v28M25 40c-8 0-14-4-14-10 8 0 14 4 14 10zM25 36c6 0 12-3 12-9-6 0-12 3-12 9z"/><line x1="12" y1="52" x2="38" y2="52"/></svg>
    <h3>Our Investment<br>Philosophy</h3>
    <p>We only invest in startups that have broad &amp; immediate applicability across a global CIO base and are solving critical problems. To give our portfolio companies a truly unfair competitive advantage, we do not invest in competitive startups.</p>
  </div>
  <div class="abs card" style="left:704px">
    <svg width="62" height="56" viewBox="0 0 62 56" fill="none" stroke="#1a7fd0" stroke-width="2"><circle cx="38" cy="18" r="15"/><circle cx="38" cy="14" r="5"/><path d="M29 28a10 10 0 0 1 18 0"/><path d="M4 36h8v16H4zM12 38l10-4h10a3 3 0 0 1 0 6H22M32 40l14-6a3 3 0 0 1 3 5L32 50H12"/></svg>
    <h3>Customer-Led<br>Investments</h3>
    <p>A global roster of CIOs leads our investment decision-making process. We also share candid, unfiltered feedback from dozens of customers via a Larkfen Memo with every single startup who presents to us - even if we don't end up investing.</p>
  </div>

  <!-- STRENGTH IN NUMBERS -->
  <div class="abs tint"></div>
  <h2 class="abs h2 center" style="left:0;width:1088px;top:1340px"><span class="hl">Strength</span> In Numbers</h2>
  <div class="abs rule" style="left:530px;top:1394px"></div>
  <div class="abs focus-label center">Investment Focus Areas</div>
  <div class="abs dots" style="left:55px;top:1440px;width:105px;height:70px"></div>
  <div class="abs dots" style="left:975px;top:1580px;width:70px;height:90px"></div>

  <div class="abs focus" style="left:113px;width:123px"><svg width="42" height="42" viewBox="0 0 42 42" fill="none" stroke="#1a7fd0" stroke-width="2"><path d="M21 3l15 6v10c0 10-7 17-15 20C13 36 6 29 6 19V9z"/><rect x="15" y="19" width="12" height="9" rx="1"/><path d="M17 19v-3a4 4 0 0 1 8 0v3"/></svg><span>SECURITY</span></div>
  <div class="abs focus" style="left:260px;width:116px"><svg width="42" height="42" viewBox="0 0 42 42" fill="none" stroke="#1a7fd0" stroke-width="2"><circle cx="16" cy="18" r="11"/><path d="M12 29v8h8v-8"/><text x="10" y="22" font-size="9" font-family="Poppins,sans-serif" fill="#1a7fd0" stroke="none" font-weight="700">AI</text><path d="M28 10h8M28 18h10M28 26h8"/><circle cx="38" cy="10" r="2"/><circle cx="38" cy="26" r="2"/></svg><span>AI &amp; ML</span></div>
  <div class="abs focus" style="left:400px;width:131px"><svg width="44" height="44" viewBox="0 0 44 44" fill="none" stroke="#1a7fd0" stroke-width="2"><circle cx="22" cy="22" r="18"/><ellipse cx="22" cy="22" rx="8" ry="18"/><line x1="4" y1="22" x2="40" y2="22"/><path d="M7 13h30M7 31h30"/></svg><span>NETWORKING &amp;<br>ARCHITECTURE</span></div>
  <div class="abs focus" style="left:555px;width:132px"><svg width="46" height="42" viewBox="0 0 46 42" fill="none" stroke="#1a7fd0" stroke-width="2"><path d="M12 26a9 9 0 0 1 1-18 11 11 0 0 1 20 2 8 8 0 0 1 1 16z"/><rect x="16" y="14" width="14" height="5"/><rect x="16" y="21" width="14" height="5"/><path d="M23 26v8M12 38h22"/></svg><span>CLOUD &amp;<br>INFRASTRUCTURE</span></div>
  <div class="abs focus" style="left:710px;width:117px"><svg width="42" height="42" viewBox="0 0 42 42" fill="none" stroke="#1a7fd0" stroke-width="2"><circle cx="27" cy="14" r="9"/><circle cx="27" cy="14" r="3"/><circle cx="14" cy="28" r="9"/><circle cx="14" cy="28" r="3"/></svg><span>DEVOPS</span></div>
  <div class="abs focus" style="left:850px;width:124px"><svg width="46" height="42" viewBox="0 0 46 42" fill="none" stroke="#1a7fd0" stroke-width="2"><path d="M11 22a9 9 0 0 1 2-18 11 11 0 0 1 20 2 8 8 0 0 1 2 16"/><text x="13" y="16" font-size="8" font-family="Poppins,sans-serif" fill="#1a7fd0" stroke="none" font-weight="700">SaaS</text><circle cx="23" cy="31" r="7"/><circle cx="23" cy="31" r="2.5"/></svg><span>SAAS</span></div>

  <p class="abs statement">We collect and analyze monthly purchase intent data from a global network of IT decision-makers.</p>

  <div class="abs" role="img" aria-label="Dotted world map backdrop" style="left:520px;top:1805px;width:470px;height:400px;border-radius:50%;background:radial-gradient(ellipse at center,#eef2f6 0%,#f7f9fb 55%,rgba(255,255,255,0) 72%)"></div>
  <div class="abs" role="img" aria-label="Low-poly wireframe illustration of a seated man pushing a rising chart line" style="left:163px;top:1955px;width:245px;height:321px;border-radius:8px;background:linear-gradient(160deg,#f1f3f6 0%,#e2e6eb 100%)"></div>
  <svg class="abs" style="left:113px;top:1735px" width="878" height="557" viewBox="100 1050 520 330" aria-hidden="true">
    <polyline points="275,1285 300,1270 345,1230 380,1245 415,1220 440,1228 470,1210 493,1175 515,1153 530,1130" fill="none" stroke="#1b1f2b" stroke-width="1.4"/>
    <g fill="#1b1f2b"><circle cx="300" cy="1270" r="1.8"/><circle cx="345" cy="1230" r="1.8"/><circle cx="380" cy="1245" r="1.8"/><circle cx="415" cy="1220" r="1.8"/><circle cx="440" cy="1228" r="1.8"/><circle cx="470" cy="1210" r="1.8"/><circle cx="493" cy="1175" r="1.8"/></g>
    <line x1="400" y1="1150" x2="470" y2="1210" stroke="#1b1f2b" stroke-width="1.2"/>
  </svg>
  <div class="abs stat" style="left:594px;top:1786px;width:162px;height:162px"><b>500+</b><small>Early adopting, influential CIOs, CTOs, CISOs and IT decision-makers</small></div>
  <div class="abs stat" style="left:811px;top:1738px;width:146px;height:146px"><b>550+</b><small>Purchase intent data points collected monthly</small></div>
  <div class="abs stat" style="left:756px;top:2009px;width:168px;height:168px"><b>$100B+</b><small>Annual enterprise technology purchasing budget across our network</small></div>
  <div class="abs stat" style="left:521px;top:2090px;width:146px;height:146px"><b>15</b><small>Countries represented in our current network</small></div>
  <div class="abs dots" style="left:0;top:2300px;width:108px;height:70px"></div>

  <h3 class="abs themes-title center">Unifying Investment Themes</h3>
  <div class="abs vrule" style="left:386px"></div>
  <div class="abs vrule" style="left:700px"></div>
  <div class="abs theme" style="left:103px"><svg width="50" height="46" viewBox="0 0 50 46" fill="none" stroke="#1a7fd0" stroke-width="2"><rect x="16" y="6" width="18" height="14" rx="1"/><path d="M20 26l5-6 5 6M3 22l8 10h10M47 22l-8 10H29M11 32v10M39 32v10"/></svg>Next-Gen Enterprise IT<br>Solutions</div>
  <div class="abs theme" style="left:393px"><svg width="50" height="46" viewBox="0 0 50 46" fill="none" stroke="#1a7fd0" stroke-width="2"><circle cx="25" cy="12" r="9"/><line x1="16" y1="12" x2="34" y2="12"/><path d="M8 42V30M16 42V26M24 42V32M32 42V24M40 42V28M4 42h42"/></svg>Attacking Large Markets With<br>Universal Application</div>
  <div class="abs theme" style="left:705px"><svg width="50" height="46" viewBox="0 0 50 46" fill="none" stroke="#1a7fd0" stroke-width="2"><circle cx="25" cy="22" r="6"/><circle cx="13" cy="9" r="4"/><circle cx="37" cy="9" r="4"/><rect x="20" y="2" width="10" height="7"/><path d="M6 42h14l-3-6M44 42H30l3-6M25 28v6"/></svg>Products And Platforms That<br>Take A Holistic Approach</div>

  <!-- TEAM -->
  <div class="abs team-bg"></div>
  <svg class="abs" style="left:0;top:3216px" width="1088" height="62" viewBox="0 0 1088 62" preserveAspectRatio="none" aria-hidden="true">
    <polygon points="0,30 1088,0 1088,30 0,52" fill="#c9d8ea"/>
    <polygon points="0,52 1088,30 1088,62 0,62" fill="#ffffff"/>
  </svg>
  <h2 class="abs team-title center">Team, Investors &amp; Advisors</h2>
  <p class="abs team-copy center">We have built a world-class roster of executive advisors and mentors with exceptional go-to-market pedigrees to help our portfolio companies in their go-to-market journeys.</p>
  <div class="abs arrow" style="left:75px">‹</div>
  <div class="abs arrow" style="left:1003px">›</div>
  <div class="abs photo" style="left:128px" role="img" aria-label="Portrait photo of Ravi N. Okoro"></div>
  <div class="abs photo" style="left:346px" role="img" aria-label="Portrait photo of Colin Marsh"></div>
  <div class="abs photo" style="left:565px" role="img" aria-label="Portrait photo of Devin Rao"></div>
  <div class="abs photo" style="left:783px" role="img" aria-label="Portrait photo of Eli Brandt"></div>
  <div class="abs person" style="left:107px"><b>Ravi N. Okoro</b><span>Founder &amp; Managing Director</span></div>
  <div class="abs person" style="left:325px"><b>Colin Marsh</b><span>Founder &amp; Ex CEO, Stonevale</span></div>
  <div class="abs person" style="left:544px"><b>Devin Rao</b><span>Co-founder, Cirrusly (IPO),<br>Quillmark</span></div>
  <div class="abs person" style="left:762px"><b>Eli Brandt</b><span>Co-founder, Tidepool Data<br>($2B+ valuation)</span></div>

  <!-- GTM ENGINE -->
  <div class="abs globe" role="img" aria-label="Dotted wireframe globe illustration in blue"></div>
  <h2 class="abs h2" style="left:543px;top:3343px"><span class="hl">A Global</span> GTM Engine</h2>
  <div class="abs rule" style="left:543px;top:3395px"></div>
  <p class="abs engine-copy">We don't just make "customer intros", we partner with you each step of the way to help you navigate the complex landscape of enterprise sales, from key strategic accounts to strategic channel partners.</p>
  <div class="abs acc" style="top:3505px">GTM Coaches <svg width="12" height="8" viewBox="0 0 12 8"><polyline points="1,7 6,2 11,7" fill="none" stroke="#1a9bd9" stroke-width="1.6"/></svg></div>
  <p class="abs acc-body">We will partner with you to navigate the complex enterprise sales process by leveraging our executive network to provide product feedback, sales strategy, and market insights.</p>
  <div class="abs hrule" style="top:3630px"></div>
  <div class="abs acc" style="top:3642px">Strategic Partners <svg width="12" height="8" viewBox="0 0 12 8"><polyline points="1,1 6,6 11,1" fill="none" stroke="#333" stroke-width="1.6"/></svg></div>
  <div class="abs hrule" style="top:3682px"></div>
  <div class="abs acc" style="top:3697px">Global Ambassadors <svg width="12" height="8" viewBox="0 0 12 8"><polyline points="1,1 6,6 11,1" fill="none" stroke="#333" stroke-width="1.6"/></svg></div>

  <!-- FOOTER -->
  <svg class="abs" style="left:0;top:3822px" width="1088" height="50" viewBox="0 0 1088 50" preserveAspectRatio="none" aria-hidden="true">
    <polygon points="0,8 1088,30 1088,50 0,50" fill="#d5d8dd"/>
    <polygon points="0,20 1088,40 1088,50 0,50" fill="#10213a"/>
  </svg>
  <footer class="abs footer"></footer>
  <div class="abs brand" style="left:444px;top:3905px"><span class="dot"></span>Larkfen Ventures</div>
  <div class="abs foot-nav" style="left:113px">About</div>
  <div class="abs foot-nav" style="left:184px">Network</div>
  <div class="abs foot-nav" style="left:265px">Team &amp; Advisors</div>
  <div class="abs foot-nav" style="left:396px">GTM Engine</div>
  <div class="abs foot-nav" style="left:499px">Contact Us</div>
  <div class="abs foot-mail">hello@larkfen-ventures.example</div>
  <div class="abs foot-rule"></div>
  <div class="abs copy center">Copyright © 2022 <b>Larkfen Ventures</b> &nbsp;|&nbsp; Privacy Policy &nbsp;|&nbsp; Terms &amp; Conditions</div>
  <p class="abs disclaimer center">Disclaimer: the content on this site is for general information only and is not an offer to sell or a solicitation to buy any security. Past performance does not guarantee future results. Investing in early-stage companies carries risk, including the loss of capital. Please consult your own advisors before making any investment decision.</p>
</div>
</body>
</html>
```